DATA PROTECTION OFFICER - GENERAL DATA PROTECTION REGULATION

Our network of companies is called : KTV (KTVR-QLM FLARES).
It is sourced and based in Brussels, Belgium, hosting the EU institutions : designers and enforcers of the GDPR (https://portal.vendrimatex.example/info/rules/privacy-notes_en).
We are setting up connected, empowered and visionary-interconnected organizations in each country, region or city concerned by the GDPR.
We have developed unique pedagogical methods, programs, instruments (video, softwares,…) and visionary training skills – initially and on a continuous basis – for the DPO & GDPR consultants.
Our motto is : From Challenges to Opportunities.
Our yearning is : developing soulful teams, join forces & talents with our clients.
Our most wanted reward : let us astonish you!
We opt for the best available softwares on the market for project management, data analytics, GDPR compliance, DPO assistance and in general : customer relation and enhanced communication between project members.
We contribute to bringing Artificial Intelligence and Data-Driven Mindsets in enterprises.
We perceive the GDPR as the best opportunity an organization faces to value its “gold” (its data) and offer the solutions to transform them into real-life currencies and assets… MONEY .
I guess my comments need time to be integrated and I provided a lot of text too! I would particularly encourage RT (UK) to take the best out of his several proposals to mix them in the best ONE website! Offering me many graphic elements to use for all my posts/pages... I am a prolix writer :)
Target Market(s)
SME's business leaders, HR and Legal departments, read : https://www.kovalnews.example/article/us-privacy-role/growth-of-the-privacy-lead-the-newest-job-in-demand-idUSKQ7ZT4PL
Industry/Entity Type
Legal
Coding
Coded - Design and coding required
Number of Pages Required
5+ page
Colors
Designer to choose colors to be used in the design.
Requirements
Must have
- A HUMAN APPROACH
- WE NEED TO SEE HUMANS AND NOT ONLY ROBOTS OR ELECTRONIC DEVICES.
- 1) The DPO/GDPR Logos of the companies:
- https://www.filtrunbox.example/sh/k82r44tbzq7nn22/BBD4maPeFhBy1pllrk5Gnnqb?dl=0
- https://www.filtrunbox.example/sh/q3x71fjzr55kzd/BBB9bjVFdde_p8mnpuBzRgs?dl=0 et DPO : https://www.filtrunbox.example/sh/t6v9k3dtp44zz7q/BBEjuYFfMvuwtxnECRC6LnmTR-b?dl=0
- OR :
- https://www.filtrunbox.example/sh/wemmdv2jr5kbzw/BBBSeYNPFeWmNEWCLO3RSg3qWb?dl=0
- AND :
- https://stewardlane.teamvault.example/sites/all/_layouts/15/guestaccess.aspx?guestaccesstoken=K4bbqw862NMTW7KhcM4Wq0p%2BScqNwdl1sqQk%2FmUmQOV%3D&folderid=2_3f71b91a29a805d81c96b8636e419f7ce&rev=1&e=6b611bf144535597b9296c99cd6116c9
- 2) A surprising but human, clear, simple, white, lightning look!
- 3) WORDPRESS version so that I can edit easily and add text on existing and new pages
- We therefore pass each option and - even more so - through the sieve of this inevitable - and values-generating - ethical evaluation.
- In other words, we are doubly satisfied with EVERY solution:
- 1. As a DPO/consultant and advisor to commercial enterprises or non-profit organisations but necessarily entering into a relationship involving financial flows with the persons concerned; and
- 2. As concerned person: target of the actions envisaged, parent, child, citizen and avatar in our digital lives.
- We put personal data at the centre of our projects and internal meetings, and with clients, we therefore continue the stage of brainstorming, researching and visualising ideas in interaction with the Regulation, by analysing the ethical consequences of each option.
- We choose only solutions that are applicable to the greatest number and therefore satisfy us as citizens of an increasingly connected and digital world. We also see the Regulation as a commercial and marketing opportunity to enhance the value of personal data and develop the confidence of those concerned by respect and security in the processing of such data.
- Our ultimate test: we put ourselves in our children's shoes to test the option considered, then comment on it and evaluate it as a parent.
- NO TO INCOMPREHENSIVE LEGAL TERMS... It is simply prohibited from 25 May for all information to be communicated to the persons concerned by the Regulation!
Nice to have
- - Artificial Intelligence
- - Transhumans
- - Challenges becoming Opportunities
- - a Great Dame who Protects & Reassures (see GDPR logo)
- - Friendly communication - NOT too businesslike/cold/usual
- - Page content is available here in FRENCH then ENGLISH then DUTCH then GERMAN : https://www.filtrunbox.example/sh/r1hgqmzsa101zwv/BBDNSzNQSFzz2qvvIZr5Ca?dl=0
Should not have
- A cold, bankerlike, old economy, dull outlook

```html
<!DOCTYPE html>
<html lang="en">
<head>
<meta charset="utf-8">
<title>KTVR-QLM Flares – From Challenges to Opportunities</title>
<link rel="stylesheet" href="https://fonts.googleapis.com/css2?family=Catamaran:wght@600;700&family=Open+Sans:wght@400;600;700&family=Fira+Sans:wght@300;400&family=Saira+Semi+Condensed:wght@500;600&display=swap">
<style>
  :root {
    --pink: #d063a8;
    --pink-band: rgba(208, 92, 165, 0.92);
    --navy-band: rgba(44, 52, 138, 0.92);
    --navy: #252b78;
    --icon-dark: #261d5a;
    --yellow: #fde100;
    --title-yellow: #ffd21f;
    --ink: #1d1d24;
    --white: #ffffff;
  }
  * { box-sizing: border-box; margin: 0; padding: 0; }
  html, body { width: 1200px; height: 1122px; overflow: hidden; background: var(--white); }
  .page { position: relative; width: 1200px; height: 1122px; overflow: hidden; font-family: "Open Sans", sans-serif; color: var(--ink); }

  .hero-visual {
    position: absolute; inset: 0 0 40px 0;
    background:
      radial-gradient(ellipse 260px 360px at 990px 420px, #f3f5f8 0%, #e3e8ef 55%, rgba(220,226,235,0) 100%),
      linear-gradient(100deg, #f4f6f9 0%, #dfe4ea 30%, #c9d1dc 55%, #aab5c4 75%, #b7c1ce 100%);
  }

  .contact-bar { position: absolute; top: 0; right: 0; width: 671px; height: 42px; }
  .contact-bar svg { position: absolute; inset: 0; }
  .contact-item { position: absolute; top: 11px; display: flex; align-items: center; gap: 7px; color: var(--white); font-weight: 600; font-size: 14px; }
  .contact-item svg { position: static; }
  .social { position: absolute; top: 11px; left: 496px; display: flex; gap: 4px; }
  .social span { width: 20px; height: 20px; border: 1.5px solid var(--white); border-radius: 50%; }
  .lang { position: absolute; top: 11px; left: 589px; display: flex; align-items: center; gap: 6px; color: var(--white); font-weight: 700; font-size: 14px; }
  .lang .dot { width: 17px; height: 17px; border-radius: 50%; background: #e8eaf2; }

  .brand { position: absolute; display: flex; align-items: center; gap: 10px; font-family: "Catamaran", sans-serif; font-weight: 700; color: var(--pink); }
  .brand-primary { left: 26px; top: 58px; font-size: 34px; }
  .brand-primary .mark { width: 30px; height: 30px; border-radius: 50%; background: var(--pink); }
  .brand-secondary { left: 250px; top: 58px; font-size: 34px; color: var(--navy); }
  .brand-secondary .mark { width: 28px; height: 28px; background: var(--navy); }

  .main-nav { position: absolute; top: 93px; left: 517px; display: flex; gap: 0; font-family: "Open Sans", sans-serif; font-weight: 600; font-size: 13.5px; letter-spacing: 0.2px; color: #1b1b22; }
  .main-nav a { color: inherit; text-decoration: none; position: absolute; white-space: nowrap; }
  .main-nav a.is-active { color: var(--pink); }
  .main-nav a.is-active::after { content: ""; position: absolute; left: 0; right: 0; top: 24px; height: 3px; background: var(--pink); }

  .intro-card { position: absolute; left: 317px; top: 269px; width: 567px; height: 246px; border: 2px solid var(--navy); border-radius: 6px; background: rgba(255,255,255,0.9); }
  .intro-card h1 { position: absolute; top: 16px; left: 0; right: 0; text-align: center; font-family: "Catamaran", sans-serif; font-weight: 700; font-size: 30px; color: var(--pink); }
  .intro-card p { position: absolute; left: 60px; top: 78px; width: 470px; font-size: 17px; line-height: 23.5px; color: #111; }
  .learn-more { position: absolute; left: 482px; top: 491px; width: 236px; height: 47px; background: var(--yellow); border-radius: 3px; display: flex; align-items: center; justify-content: center; font-family: "Catamaran", sans-serif; font-weight: 700; font-size: 21px; color: #2a2638; text-decoration: none; }

  .feature-band { position: absolute; left: 0; top: 640px; width: 1200px; height: 442px; }
  .feature-band > svg { position: absolute; inset: 0; }
  .feature { position: absolute; top: 0; width: 300px; height: 442px; color: var(--white); }
  .feature h2 { position: absolute; left: 22px; top: 170px; font-family: "Saira Semi Condensed", sans-serif; font-weight: 600; font-size: 20px; color: var(--title-yellow); }
  .feature p { position: absolute; left: 22px; top: 196px; width: 270px; font-family: "Fira Sans", sans-serif; font-weight: 300; font-size: 15.5px; line-height: 20.8px; }
  .feature .go { position: absolute; left: 21px; top: 368px; width: 26px; height: 26px; border-radius: 50%; border: 2px solid var(--white); display: flex; align-items: center; justify-content: center; }
  .go.yellow { background: var(--yellow); }
  .go.pink { background: #e9559b; }
  .feature-icon { position: absolute; width: 88px; height: 88px; }

  .site-footer { position: absolute; left: 0; bottom: 0; width: 1200px; height: 40px; background: var(--white); display: flex; align-items: center; justify-content: center; font-size: 12.5px; font-weight: 600; color: #2a2a30; letter-spacing: 0.2px; }
</style>
</head>
<body>
<div class="page">
  <div class="hero-visual" role="img" aria-label="Photograph of a friendly white humanoid robot with glowing blue eyes in a bright meeting room with chairs and tall windows"></div>

  <div class="contact-bar">
    <svg width="671" height="42" viewBox="0 0 671 42"><polygon points="0,0 671,0 671,42 42,42" fill="var(--pink)"/></svg>
    <div class="contact-item" style="left:77px">
      <svg width="22" height="22" viewBox="0 0 22 22"><circle cx="11" cy="11" r="10" fill="none" stroke="#fff" stroke-width="1.5"/><path d="M7.5 6.5l2 0 1 2.5-1.3 1a6 6 0 0 0 2.8 2.8l1-1.3 2.5 1v2a1 1 0 0 1-1 1A8 8 0 0 1 6.5 7.5a1 1 0 0 1 1-1z" fill="#fff"/></svg>
      +32 2 555 01 47
    </div>
    <div class="contact-item" style="left:252px">
      <svg width="22" height="22" viewBox="0 0 22 22"><circle cx="11" cy="11" r="10" fill="none" stroke="#fff" stroke-width="1.5"/><rect x="6" y="7.5" width="10" height="7" fill="none" stroke="#fff" stroke-width="1.3"/><path d="M6 7.5l5 4 5-4" fill="none" stroke="#fff" stroke-width="1.3"/></svg>
      info@ktvr-qlmflares.example
    </div>
    <div class="social"><span></span><span></span><span></span></div>
    <div class="lang"><span class="dot"></span>EN
      <svg width="10" height="7" viewBox="0 0 10 7"><path d="M1 1l4 4 4-4" fill="none" stroke="#fff" stroke-width="1.6"/></svg>
    </div>
  </div>

  <div class="brand brand-primary"><span class="mark"></span>KTVR</div>
  <div class="brand brand-secondary"><span class="mark"></span>QLM Flares</div>

  <nav class="main-nav">
    <a class="is-active" href="#" style="left:0">HOME</a>
    <a href="#" style="left:62px">ABOUT</a>
    <a href="#" style="left:133px">SERVICES</a>
    <a href="#" style="left:222px">OUR VISION</a>
    <a href="#" style="left:326px">DPO SCHOOLS</a>
    <a href="#" style="left:449px">AI &amp; SOFTWARES</a>
    <a href="#" style="left:590px">CONTACT</a>
  </nav>

  <section class="intro-card">
    <h1>From Challenges to Opportunities</h1>
    <p>Sourced and based in Brussels, Belgium, hosting the EU institutions : designers and enforcers of the GDPR. We are setting up connected, empowered and visionary-interconnected organizations in each country, region or city concerned by the GDPR based on the TEAL approach .</p>
  </section>
  <a class="learn-more" href="#">Learn More</a>

  <section class="feature-band">
    <svg width="1200" height="442" viewBox="0 0 1200 442">
      <polygon points="0,45 300,60.5 300,442 0,442" fill="var(--pink-band)"/>
      <polygon points="300,60.5 600,76 600,442 300,442" fill="var(--navy-band)"/>
      <polygon points="600,76 900,91.5 900,442 600,442" fill="var(--pink-band)"/>
      <polygon points="900,91.5 1200,107 1200,442 900,442" fill="var(--navy-band)"/>
    </svg>

    <svg class="feature-icon" style="left:105px;top:6px" viewBox="0 0 88 88"><circle cx="44" cy="44" r="43" fill="rgba(235,225,240,0.55)"/><circle cx="44" cy="44" r="34" fill="var(--icon-dark)"/><rect x="31" y="31" width="11" height="11" fill="none" stroke="#fff" stroke-width="2.2"/><rect x="42" y="31" width="11" height="11" fill="#fff"/><rect x="31" y="42" width="11" height="11" fill="#fff"/><path d="M48 46v12h8l-3-8z" fill="#fff"/></svg>
    <svg class="feature-icon" style="left:405px;top:20px" viewBox="0 0 88 88"><circle cx="44" cy="44" r="43" fill="rgba(190,195,215,0.5)"/><circle cx="44" cy="44" r="34" fill="#1e1e26"/><path d="M32 44a12 12 0 0 1 24 0c0 6-3 8-3 12H35c0-4-3-6-3-12z" fill="none" stroke="#fff" stroke-width="2.2"/><path d="M44 34v22M38 40l6 5 6-5M38 50h12" fill="none" stroke="#fff" stroke-width="1.8"/></svg>
    <svg class="feature-icon" style="left:705px;top:34px" viewBox="0 0 88 88"><circle cx="44" cy="44" r="43" fill="rgba(235,225,240,0.55)"/><circle cx="44" cy="44" r="34" fill="var(--icon-dark)"/><path d="M44 28l13 5v9c0 9-6 15-13 18-7-3-13-9-13-18v-9z" fill="none" stroke="#fff" stroke-width="2.4"/><path d="M39 48l10-10M37 42l6-6M44 52l8-8" stroke="#fff" stroke-width="2"/></svg>
    <svg class="feature-icon" style="left:1006px;top:53px" viewBox="0 0 88 88"><circle cx="44" cy="44" r="43" fill="rgba(190,195,215,0.5)"/><circle cx="44" cy="44" r="34" fill="#1e1e26"/><path d="M31 57l8-8M39 49l-2-6 10-10 8 8-10 10z" fill="none" stroke="#fff" stroke-width="2.4" stroke-linejoin="round"/><path d="M47 33l5-5M55 41l5-5" stroke="#fff" stroke-width="2.4"/></svg>

    <article class="feature" style="left:0">
      <h2>About</h2>
      <p>Lorem ipsum dolor sit amet, consec tetuer adipiscing elit, sed diam non ummy nibh euismod tincidunt ut lao reet dolore magna aliquam erat vol utpat. Ut wisi enim ad minim veniam, quis nostrud exerci tation ullamcor per suscipit lobortis nisl ut aliquip ex ea commodo consequat.</p>
      <a class="go yellow" href="#"><svg width="12" height="12" viewBox="0 0 12 12"><path d="M1 6h9M6.5 2.5L10 6l-3.5 3.5" fill="none" stroke="#fff" stroke-width="1.8"/></svg></a>
    </article>
    <article class="feature" style="left:300px">
      <h2>Services</h2>
      <p>Lorem ipsum dolor sit amet, consec tetuer adipiscing elit, sed diam non ummy nibh euismod tincidunt ut lao reet dolore magna aliquam erat vol utpat. Ut wisi enim ad minim veniam, quis nostrud exerci tation.</p>
      <a class="go pink" href="#"><svg width="12" height="12" viewBox="0 0 12 12"><path d="M1 6h9M6.5 2.5L10 6l-3.5 3.5" fill="none" stroke="#fff" stroke-width="1.8"/></svg></a>
    </article>
    <article class="feature" style="left:600px">
      <h2>DPO Schools</h2>
      <p>Lorem ipsum dolor sit amet, consec tetuer adipiscing elit, sed diam non ummy nibh euismod tincidunt ut lao reet dolore magna aliquam erat vol utpat. Ut wisi enim ad minim veniam, quis nostrud exerci tation ullamcor per suscipit lobortis.</p>
      <a class="go yellow" href="#"><svg width="12" height="12" viewBox="0 0 12 12"><path d="M1 6h9M6.5 2.5L10 6l-3.5 3.5" fill="none" stroke="#fff" stroke-width="1.8"/></svg></a>
    </article>
    <article class="feature" style="left:900px">
      <h2>AI &amp; Softwares</h2>
      <p>Lorem ipsum dolor sit amet, consec tetuer adipiscing elit, sed diam non ummy nibh euismod tincidunt ut lao reet dolore magna aliquam erat vol utpat. Ut wisi enim ad minim veniam, quis nostrud exerci tation ullamcor per suscipit.</p>
      <a class="go pink" href="#"><svg width="12" height="12" viewBox="0 0 12 12"><path d="M1 6h9M6.5 2.5L10 6l-3.5 3.5" fill="none" stroke="#fff" stroke-width="1.8"/></svg></a>
    </article>
  </section>

  <footer class="site-footer">COPYRIGHT © 2018 KTVR-QLM. ALL RIGHTS RESERVED.</footer>
</div>
</body>
</html>
```